Door Company flyer for hardware sale

I need a flyer approximately 4" wide by 5" height. I need to promote one of the brands we carry (MARLOW) for a one day discount sale on Wednesday May 22, 2024. Our company name is TULVEN Commercial Door and our main vendor is Corvanta but we will have special pricing on MARLOW products which are the 3 pictures of hardware. I would like for the date to stand out in a different color. I want to use our logo colors which are gray, orange, and white but would like the date in a banner of a different color. We also want to add that we will have free tacos, prizes, and goodies.

Target Market(s)

Construction Industry

Industry/Entity Type

Construction

Colors
F0912C
F2A743
F7CA91
FBE8D2
FDF5EE
EE7325
F08F49
F5BC92
FAE3D3
FDF4ED

Requirements
Must have
• Pictures of hardware & logos I uploaded. Invite customers to join us for special pricing, free tacos, prizes and more.
Nice to have
• Promote the May 22 2024 event

```html
<!DOCTYPE html>
<html lang="en">
<head>
<meta charset="utf-8">
<title>TULVEN Commercial Door – One Day Discount Sale</title>
<link rel="stylesheet" href="https://fonts.googleapis.com/css2?family=Anton&family=Lexend:wght@400;500;600&display=swap">
<style>
  :root {
    --page-bg: #c4c4c4;
    --paper: #ffffff;
    --ink: #333333;
    --ink-soft: #4a4a4a;
    --brand-gray: #6b6e70;
    --ribbon: #2f2f2f;
    --ribbon-fold: #161616;
    --date-blue: #1450d2;
    --orange: #f39321;
    --orange-deep: #ee7325;
    --panel-light: #f4f4f4;
    --panel-mid: #d6d6d6;
    --rule: #8a8a8a;
  }
  * { box-sizing: border-box; margin: 0; padding: 0; }
  html, body { width: 1200px; height: 2303px; overflow: hidden; }
  body {
    background: var(--page-bg);
    font-family: "Lexend", sans-serif;
    color: var(--ink);
    position: relative;
  }
  .flyer {
    position: absolute;
    left: 100px; top: 526px;
    width: 1000px; height: 1250px;
    background: var(--paper);
    box-shadow: 0 24px 40px rgba(0,0,0,.25);
  }
  .flyer > * { position: absolute; }

  /* brand header */
  .brand {
    left: 0; width: 654px; top: 70px;
    display: flex; justify-content: center; align-items: center; gap: 18px;
    color: var(--brand-gray);
  }
  .brand-mark { width: 52px; height: 52px; background: var(--orange); }
  .brand-name { font-weight: 600; font-size: 40px; line-height: 1.05; letter-spacing: 2px; }
  .brand-name small { display: block; font-size: 17px; letter-spacing: 3px; font-weight: 600; }

  /* ribbon + date */
  .sale-ribbon { left: 56px; top: 234px; width: 544px; height: 66px; }
  .sale-ribbon span {
    position: absolute; inset: 0;
    display: flex; align-items: center; justify-content: center;
    font-family: "Anton", sans-serif; color: #fff; font-size: 40px; letter-spacing: .5px;
  }
  .event-day, .event-date {
    left: 0; width: 654px; text-align: center;
    font-family: "Anton", sans-serif; color: var(--date-blue);
    text-transform: uppercase; line-height: 1;
  }
  .event-day { top: 312px; font-size: 92px; letter-spacing: 1px; }
  .event-date { top: 400px; font-size: 140px; letter-spacing: 4px; }
  .divider { left: 58px; top: 563px; width: 540px; height: 2px; background: var(--rule); }
  .invite {
    left: 0; width: 654px; top: 582px; text-align: center;
    font-size: 27px; line-height: 1.42; color: var(--ink-soft);
  }

  /* feature band */
  .features {
    left: 0; top: 710px; width: 672px; height: 209px;
    background: var(--orange);
    display: flex; align-items: center;
  }
  .feature {
    flex: 1; display: flex; flex-direction: column; align-items: center; gap: 16px;
    color: #fff; font-weight: 600; font-size: 31px;
  }
  .feature + .feature { border-left: 2px solid rgba(255,255,255,.6); }
  .feature svg { width: 86px; height: 86px; }

  /* vendors */
  .vendors {
    left: 0; width: 654px; top: 960px;
    display: flex; justify-content: center; align-items: center; gap: 26px;
    font-weight: 600; font-size: 36px; color: var(--ink); letter-spacing: 2px;
  }
  .vendor { display: flex; align-items: center; gap: 12px; }
  .vendor-mark { width: 40px; height: 40px; background: var(--orange-deep); }
  .vendor-sep { width: 2px; height: 44px; background: var(--rule); }

  /* contact */
  .phone {
    left: 72px; top: 1043px; width: 508px; height: 72px;
    background: var(--orange); border-radius: 36px;
    display: flex; align-items: center; justify-content: center; gap: 14px;
    color: #fff; font-weight: 600; font-size: 50px;
  }
  .phone svg { width: 40px; height: 40px; }
  .contact-line {
    left: 0; width: 654px; text-align: center;
    font-weight: 500; font-size: 29px; color: var(--ink);
  }
  .email { top: 1134px; }
  .web { top: 1178px; }

  /* product column */
  .product {
    left: 654px; width: 346px;
    background: radial-gradient(circle at 55% 40%, var(--panel-light) 0%, var(--panel-mid) 100%);
  }
  .product-closers { top: 0; height: 409px; }
  .product-locks { top: 423px; height: 409px; left: 672px; width: 328px; }
  .product-exits { top: 845px; height: 405px; left: 672px; width: 328px; }
  .product-label {
    position: absolute; left: 0; right: 0; bottom: 40px; text-align: center;
    font-weight: 500; font-size: 31px; color: var(--ink);
  }
</style>
</head>
<body>
  <main class="flyer">
    <header class="brand">
      <div class="brand-mark"></div>
      <div class="brand-name">TULVEN<small>COMMERCIAL DOOR</small></div>
    </header>

    <div class="sale-ribbon">
      <svg width="544" height="66" viewBox="0 0 544 66" aria-hidden="true">
        <polygon points="0,8 40,8 40,66 0,66 18,37" fill="var(--ribbon-fold)"/>
        <polygon points="544,8 504,8 504,66 544,66 526,37" fill="var(--ribbon-fold)"/>
        <rect x="28" y="0" width="488" height="58" fill="var(--ribbon)"/>
      </svg>
      <span>ONE DAY DISCOUNT SALE</span>
    </div>

    <div class="event-day">Wednesday</div>
    <div class="event-date">May 22</div>
    <div class="divider"></div>
    <p class="invite">join us for special pricing, free tacos,<br>prizes, goodies and more.</p>

    <section class="features">
      <div class="feature">
        <svg viewBox="0 0 86 86" aria-hidden="true">
          <circle cx="43" cy="43" r="32" fill="none" stroke="#fff" stroke-width="14" stroke-dasharray="10 6"/>
          <circle cx="43" cy="43" r="24" fill="#fff"/>
          <polyline points="31,44 40,53 56,35" fill="none" stroke="var(--orange)" stroke-width="7" stroke-linecap="round" stroke-linejoin="round"/>
        </svg>
        Quality
      </div>
      <div class="feature">
        <svg viewBox="0 0 86 86" aria-hidden="true">
          <polygon points="43,6 78,22 43,38 8,22" fill="#fff"/>
          <polygon points="6,28 40,44 40,82 6,64" fill="#fff"/>
          <polygon points="80,28 46,44 46,82 80,64" fill="#fff"/>
        </svg>
        Design
      </div>
      <div class="feature">
        <svg viewBox="0 0 86 86" aria-hidden="true">
          <rect x="8" y="4" width="30" height="78" rx="15" fill="#fff"/>
          <circle cx="23" cy="66" r="6" fill="var(--orange)"/>
          <polygon points="44,40 62,14 82,30 82,82 44,82" fill="#fff"/>
        </svg>
        Variety
      </div>
    </section>

    <div class="vendors">
      <div class="vendor">CORVANTA<span class="vendor-mark"></span></div>
      <span class="vendor-sep"></span>
      <div class="vendor">MARLOW</div>
    </div>

    <div class="phone">
      <svg viewBox="0 0 24 24" aria-hidden="true"><path fill="#fff" d="M6.6 10.8a15.1 15.1 0 0 0 6.6 6.6l2.2-2.2c.3-.3.7-.4 1-.2 1.1.4 2.3.6 3.6.6.6 0 1 .4 1 1V20c0 .6-.4 1-1 1A17 17 0 0 1 3 4c0-.6.4-1 1-1h3.5c.6 0 1 .4 1 1 0 1.3.2 2.5.6 3.6.1.3 0 .7-.2 1z"/></svg>
      555-214-0187
    </div>
    <div class="contact-line email">sales@tulvencommercialdoor.com</div>
    <div class="contact-line web">www.tulvencommercialdoor.com</div>

    <figure class="product product-closers" role="img" aria-label="Photo of a silver overhead door closer">
      <figcaption class="product-label">Door Closers</figcaption>
    </figure>
    <figure class="product product-locks" role="img" aria-label="Photo of a silver lever door lock">
      <figcaption class="product-label">Door Locks</figcaption>
    </figure>
    <figure class="product product-exits" role="img" aria-label="Photo of two silver push-bar exit devices">
      <figcaption class="product-label">Exit Devices</figcaption>
    </figure>
  </main>
</body>
</html>
```